Solar appointment reminder card

We are looking for a new design for our appointment reminder card since we have changed our logo. The card should have the new logo along with space for the employee to hand write the customers appointment date, time, the employees name and phone number.
I've uploaded what our old basic appointment card looked like and our new logo.

The cards should be in a standard business card size and could be horizontal or vertical.

```html
<!DOCTYPE html>
<html lang="en">
<head>
<meta charset="UTF-8">
<title>Hudson Ray Solar – Appointment Card</title>
<link rel="stylesheet" href="https://fonts.googleapis.com/css2?family=Tinos:wght@400;700&display=swap">
<style>
  :root {
    --navy: #060f35;
    --orange: #f7901e;
    --gold: #fcc12d;
    --field-bg: #ffffff;
    --field-border: #4b4b4b;
    --ink: #111111;
  }
  * { box-sizing: border-box; margin: 0; padding: 0; }
  html, body {
    width: 1200px;
    height: 667px;
    overflow: hidden;
    background: var(--orange);
  }
  .card {
    position: relative;
    width: 1200px;
    height: 667px;
    background: var(--orange);
    font-family: "Tinos", "Times New Roman", serif;
  }
  .card-header {
    position: absolute;
    left: 0; top: 0;
    width: 1200px;
    height: 203px;
    background: var(--navy);
  }
  .brand {
    position: absolute;
    left: 50px;
    top: 72px;
    display: flex;
    align-items: center;
    gap: 16px;
  }
  .brand-dot {
    width: 58px;
    height: 58px;
    border-radius: 50%;
    background: var(--gold);
  }
  .brand-name {
    color: var(--orange);
    font-weight: 700;
    font-size: 34px;
    line-height: 1;
    letter-spacing: 0.5px;
  }
  .card-title {
    position: absolute;
    right: 65px;
    top: 70px;
    color: var(--gold);
    font-weight: 700;
    font-size: 66px;
    line-height: 1;
  }
  .field {
    position: absolute;
    height: 98px;
    background: var(--field-bg);
    border: 3px solid var(--field-border);
    display: flex;
    align-items: center;
    padding-left: 13px;
    color: var(--ink);
    font-size: 34px;
  }
  .field-date  { left: 63px;  top: 247px; width: 526px; }
  .field-time  { left: 606px; top: 247px; width: 526px; }
  .field-staff { left: 63px;  top: 367px; width: 1069px; }
  .field-phone { left: 63px;  top: 487px; width: 1069px; }
</style>
</head>
<body>
  <main class="card">
    <header class="card-header">
      <div class="brand">
        <span class="brand-dot"></span>
        <span class="brand-name">Hudson Ray Solar</span>
      </div>
      <h1 class="card-title">Appoinment</h1>
    </header>
    <div class="field field-date">Date :</div>
    <div class="field field-time">Time :</div>
    <div class="field field-staff">Employees name :</div>
    <div class="field field-phone">Phone number :</div>
  </main>
</body>
</html>
```